Business Card Design Project

We require business cards for "Venmoor". We are composed of elite prior military personnel. Our goal is to provide site security for premium businesses who want on the most professional of agents on their premises. Additionally, we will provide executive protection for individuals who require professionalism, flexibility, and dedication

We want this business card to communicate professionalism, dependability, strength. However, we are not an overtly tactical agency and do not want to intimidate our clients personnel or their client. We want to give them a sense of security.
Updates

At the request of one of the designers I've listed the appropriate text that should appear on the card. Please feel free to arrange it in a creative and professional manor.

I've also uploaded a .png file of the triangle logo with no text. Please feel free to incorporate this into your designs.

ThanksĀ 

Target Market(s)

Premium businesses, executives, celebrities, and governments.

Industry/Entity Type

Security

Requirements
Must have
• Text Info that will go on the card. It does not have to be in this order:
Name
Title
Office Phone Number
Cell Phone Number
Email
Website
Mailing Address
Nice to have
• On the back I'd like to see the triangle portion of the logo displayed in a creative way that leaves enough room to write down information if needed.
Should not have
• - Weapons, Globes, or Shields. Every rent-a-cop company has that, and that's not what we are.

```html
<!DOCTYPE html>
<html lang="en">
<head>
<meta charset="utf-8">
<title>Venmoor Business Card</title>
<link rel="stylesheet" href="https://fonts.googleapis.com/css2?family=PT+Sans:wght@400;700&display=swap">
<style>
  :root {
    --stage: #e4e4e4;
    --paper: #ffffff;
    --ink-dark: #333333;
    --ink-grey: #7a7a7a;
    --brand-blue: #0a6fb3;
    --brand-blue-deep: #0d5a9c;
    --brand-blue-light: #2a9ad8;
    --rule: #8a8a8a;
  }
  * { margin: 0; padding: 0; box-sizing: border-box; }
  html, body { width: 1200px; height: 448px; overflow: hidden; }
  body {
    background: var(--stage);
    font-family: "PT Sans", Arial, sans-serif;
    position: relative;
  }
  .card {
    position: absolute;
    left: 78px; top: 75px;
    width: 1044px; height: 297px;
    background: var(--paper);
    overflow: hidden;
  }
  .feature-graphic {
    position: absolute;
    left: 424px; top: 0;
    width: 354px; height: 100%;
    background: linear-gradient(135deg, var(--brand-blue-deep) 0%, var(--brand-blue) 45%, var(--brand-blue-light) 75%, var(--brand-blue-deep) 100%);
  }
  .card-divider {
    position: absolute;
    left: 520px; top: 0;
    width: 1px; height: 100%;
    background: var(--rule);
  }
  .brand {
    position: absolute;
    left: 29px; top: 21px;
    display: flex; align-items: center; gap: 20px;
  }
  .brand-square {
    width: 44px; height: 44px;
    background: var(--brand-blue);
  }
  .brand-name {
    font-weight: 700;
    font-size: 48px;
    letter-spacing: 1px;
    color: var(--ink-dark);
    line-height: 1;
  }
  .holder {
    position: absolute;
    left: 94px; top: 127px;
  }
  .holder-name {
    font-size: 17.5px;
    color: var(--brand-blue);
    line-height: 21px;
  }
  .holder-title {
    font-size: 14px;
    color: var(--ink-grey);
    line-height: 17px;
  }
  .contact {
    position: absolute;
    left: 98px;
    list-style: none;
    font-size: 14px;
    color: var(--ink-grey);
  }
  .contact li {
    display: flex; align-items: center; gap: 6px;
    height: 17.5px;
  }
  .contact svg { width: 11px; height: 11px; fill: var(--brand-blue); flex: none; }
  .contact-direct { top: 178px; }
  .contact-office { top: 231px; }
  .contact .indent { padding-left: 17px; }
  .contact .spacer { width: 2px; }
  .website {
    position: absolute;
    left: 821px; top: 137px;
    font-size: 16px;
    color: var(--ink-grey);
  }
  .website strong { font-weight: 400; color: var(--brand-blue); }
</style>
</head>
<body>
  <div class="card">
    <div class="feature-graphic" role="img" aria-label="Large blue brand graphic spanning the fold between front and back of the card"></div>

    <section class="card-front">
      <div class="brand">
        <div class="brand-square"></div>
        <div class="brand-name">VENMOOR</div>
      </div>

      <div class="holder">
        <div class="holder-name">CARDHOLDER NAME</div>
        <div class="holder-title">Designation</div>
      </div>

      <ul class="contact contact-direct">
        <li>
          <svg viewBox="0 0 12 12"><path d="M3 0h6a1 1 0 0 1 1 1v10a1 1 0 0 1-1 1H3a1 1 0 0 1-1-1V1a1 1 0 0 1 1-1zm0 1.5v7.5h6V1.5zM6 9.6a.8.8 0 1 0 0 1.6.8.8 0 0 0 0-1.6z"/></svg>
          +012 3456 7890
        </li>
        <li>
          <svg viewBox="0 0 12 12"><path d="M0 2h12v8H0zm1.5 1.5v1h1v-1zm2 0v1h1v-1zm2 0v1h1v-1zm2 0v1h1v-1zm2 0v1h1v-1zM1.5 5.5v1h1v-1zm2 0v1h1v-1zm2 0v1h1v-1zm2 0v1h1v-1zm2 0v1h1v-1zM3 7.5v1h6v-1z"/></svg>
          cardholder.name@venmoor.com
        </li>
      </ul>

      <ul class="contact contact-office">
        <li>
          <svg viewBox="0 0 12 12"><path d="M6 0a4 4 0 0 1 4 4c0 3-4 8-4 8S2 7 2 4a4 4 0 0 1 4-4zm0 2.3a1.7 1.7 0 1 0 0 3.4 1.7 1.7 0 0 0 0-3.4z"/></svg>
          01 Sunset Avenue, Suite No. 123,
        </li>
        <li class="indent">Your City, Code, Country</li>
        <li>
          <svg viewBox="0 0 12 12"><circle cx="6" cy="6" r="6"/><path d="M3.6 3.2l1.2-.4.8 1.6-.7.6a4 4 0 0 0 1.9 1.9l.6-.7 1.6.8-.4 1.2c-3 .3-5.3-2-5-5z" fill="#fff"/></svg>
          +012 345 6789
          <span class="spacer"></span>
          <svg viewBox="0 0 12 12"><path d="M3 0h5l2 2v3H3zM1 5h10v6H1zm2 2v1h2V7zm0 2v1h2V9zm4-2v3h2V7z"/></svg>
          +012 345 6780
        </li>
      </ul>
    </section>

    <div class="card-divider"></div>

    <section class="card-back">
      <div class="website">www.<strong>VENMOOR</strong>.com</div>
    </section>
  </div>
</body>
</html>
```